goal design

We are rolling out a goal for the next 3 years. the goal is as follows:
2014: $8 million gross profit, $1.25 million net income
2015: $12 million gross profit, $2.4 million net income
2016 $15 million gross profit, $4 million net income
We want a design that captures these numbers and that we can publish company wide that will quickly remind everyone of these goals. Our website is www.brookvalerecruiting.example. This will be an internal campaign. We will use the simple design to remind our people of our goals for the next 3 years. We will print it on mouse pads, shirts and things of this nature periodically to keep it front of mind for our people. So easy to remember, visually appealing and simple are good guidelines.
Updates
Target Market(s)
This is an internal campaign. it is to remind our people of our goals for the next few years so will be on little reminder items (i.e. cell phone covers, mouse pads, shirts, screen savers, etc).
Industry/Entity Type
It Company
Look and feel

```html
<!DOCTYPE html>
<html lang="en">
<head>
<meta charset="utf-8">
<title>Three-Year Goals</title>
<link href="https://fonts.googleapis.com/css2?family=Bebas+Neue&display=swap" rel="stylesheet">
<style>
  :root {
    --bg: #1b1a17;
    --ink: #1c1a16;
    --gold-edge: #4e3219;
    --gold-deep: #9a6526;
    --gold-mid: #d9a53f;
    --gold-bright: #f8dc6e;
    --gold-pale: #fbe99a;
  }
  * { margin: 0; padding: 0; box-sizing: border-box; }
  html, body { width: 1200px; height: 1088px; overflow: hidden; background: var(--bg); }
  .canvas { position: relative; width: 1200px; height: 1088px; background: var(--bg); font-family: "Bebas Neue", "Oswald", sans-serif; color: var(--ink); }
  .goal-bar {
    position: absolute; top: 133px; width: 304px; height: 822px;
    background:
      linear-gradient(180deg, rgba(255,240,170,.18) 0%, rgba(0,0,0,0) 30%, rgba(0,0,0,0) 75%, rgba(60,30,0,.15) 100%),
      linear-gradient(90deg, var(--gold-edge) 0%, var(--gold-deep) 6%, var(--gold-mid) 16%, var(--gold-bright) 32%, var(--gold-mid) 48%, var(--gold-pale) 62%, var(--gold-mid) 78%, var(--gold-deep) 92%, var(--gold-edge) 100%);
  }
  .goal-bar--2014 { left: 112px; }
  .goal-bar--2015 { left: 448px; }
  .goal-bar--2016 { left: 784px; }
  .goal-frame {
    position: absolute; left: 26px; right: 26px; top: 27px; bottom: 27px;
    border: 3px solid var(--ink);
    box-shadow: inset 0 0 0 4px rgba(255,235,150,.35), inset 0 0 0 6px rgba(28,26,22,.8);
  }
  .goal-text {
    position: absolute; left: 0; right: 0; text-align: center; line-height: 1;
    white-space: nowrap; text-shadow: 0 1px 0 rgba(255,240,180,.45);
  }
  .goal-year { top: 66px; font-size: 137px; }
  .goal-rule { position: absolute; top: 195px; left: 52px; width: 200px; height: 3px; background: var(--ink); }
  .goal-gross-amount { top: 202px; font-size: 205px; letter-spacing: -2px; }
  .goal-unit { font-size: 88px; letter-spacing: -1px; }
  .goal-unit--gross { top: 377px; }
  .goal-unit--net { top: 652px; }
  .goal-label { font-size: 49px; letter-spacing: -0.5px; }
  .goal-label--gross { top: 449px; }
  .goal-label--net { top: 721px; font-size: 52px; }
  .goal-net-amount { top: 509px; font-size: 137px; letter-spacing: -1px; }
</style>
</head>
<body>
<main class="canvas">
  <section class="goal-bar goal-bar--2014">
    <div class="goal-frame"></div>
    <div class="goal-text goal-year">2014</div>
    <div class="goal-rule"></div>
    <div class="goal-text goal-gross-amount">$8</div>
    <div class="goal-text goal-unit goal-unit--gross">Million</div>
    <div class="goal-text goal-label goal-label--gross">Gross Profit</div>
    <div class="goal-text goal-net-amount">$1.25</div>
    <div class="goal-text goal-unit goal-unit--net">Million</div>
    <div class="goal-text goal-label goal-label--net">Net Income</div>
  </section>
  <section class="goal-bar goal-bar--2015">
    <div class="goal-frame"></div>
    <div class="goal-text goal-year">2015</div>
    <div class="goal-rule"></div>
    <div class="goal-text goal-gross-amount">$12</div>
    <div class="goal-text goal-unit goal-unit--gross">Million</div>
    <div class="goal-text goal-label goal-label--gross">Gross Profit</div>
    <div class="goal-text goal-net-amount">$2.4</div>
    <div class="goal-text goal-unit goal-unit--net">Million</div>
    <div class="goal-text goal-label goal-label--net">Net Income</div>
  </section>
  <section class="goal-bar goal-bar--2016">
    <div class="goal-frame"></div>
    <div class="goal-text goal-year">2016</div>
    <div class="goal-rule"></div>
    <div class="goal-text goal-gross-amount">$15</div>
    <div class="goal-text goal-unit goal-unit--gross">Million</div>
    <div class="goal-text goal-label goal-label--gross">Gross Profit</div>
    <div class="goal-text goal-net-amount">$4</div>
    <div class="goal-text goal-unit goal-unit--net">Million</div>
    <div class="goal-text goal-label goal-label--net">Net Income</div>
  </section>
</main>
</body>
</html>
```